Family Ranch with a hobby vineyard needs 2 wine labels for our first harvest

Design 2 wine labels (front and back) with the Brindor Ranch logo.
Label 1:
Sauvignon Blanc
Alc. 12.5% by Vol.
Palos Verdes Peninsula - add as the region
Year 2022
Label 2:
Cabernet Sauvignon
Alc. 13.5% by Vol.
Year 2022
For the back label design:
GOVERNMENT WARNING: (1) According to the Surgeon General, women
should not drink alcoholic beverages during pregnancy because of the risk of
birth defects. (2) Consumption of alcoholic beverages impairs your ability to
drive a car or operate machinery, and may cause health problems.
Contains Sulfates.
750ML
I just received the bottles and have attached a picture.
Look and feel
Each slider illustrates characteristics of the customer's brand and the style your logo design should communicate.

```html
<!DOCTYPE html>
<html lang="en">
<head>
<meta charset="utf-8">
<title>Brindor Ranch – Wine Labels</title>
<link rel="stylesheet" href="https://fonts.googleapis.com/css2?family=Oswald:wght@400;500&family=Libre+Baskerville:wght@400;700&display=swap">
<style>
  :root {
    --page: #eceae6;
    --cream: #f4e8c6;
    --ink: #231f20;
    --wine-red: #c8202b;
    --gold: #c9a96a;
    --gold-text: #ead9ab;
    --ornament: #8c8068;
  }
  * { box-sizing: border-box; margin: 0; padding: 0; }
  html, body { width: 1200px; height: 960px; overflow: hidden; }
  body {
    background: var(--page);
    display: flex;
    align-items: center;
    justify-content: space-evenly;
    font-family: "Libre Baskerville", Georgia, serif;
  }
  .label {
    position: relative;
    width: 340px;
    height: 510px;
    box-shadow: 0 4px 10px rgba(0,0,0,.18);
  }
  /* front label */
  .label--front { background: var(--cream); color: var(--ink); }
  .label__frame {
    position: absolute; inset: 18px;
    border: 3px solid var(--ink);
    border-radius: 6px;
  }
  .label__frame::after {
    content: ""; position: absolute; inset: 8px;
    border: 1px solid var(--ink);
    border-radius: 40px;
  }
  .corner-ornament {
    position: absolute; width: 52px; height: 52px;
    background: var(--ornament);
  }
  .corner-ornament--tl { top: 12px; left: 12px; }
  .corner-ornament--tr { top: 12px; right: 12px; }
  .corner-ornament--bl { bottom: 12px; left: 12px; }
  .corner-ornament--br { bottom: 12px; right: 12px; }
  .front__content {
    position: absolute; inset: 0;
    display: flex; flex-direction: column; align-items: center;
    padding-top: 70px;
  }
  .brand-mark {
    display: flex; flex-direction: column; align-items: center; gap: 10px;
  }
  .brand-mark__dot {
    width: 46px; height: 46px; border-radius: 50%;
    background: var(--ink);
  }
  .brand-mark__name {
    font-family: "Oswald", sans-serif; font-weight: 400;
    font-size: 25px; letter-spacing: 2px; color: var(--ink);
    text-transform: uppercase; line-height: 1;
  }
  .varietal {
    margin-top: 28px;
    font-family: "Oswald", sans-serif; font-weight: 500;
    font-size: 26px; color: var(--wine-red);
    letter-spacing: 0; line-height: 1;
    white-space: nowrap;
  }
  .region {
    margin-top: 18px;
    font-weight: 700; font-size: 13px; letter-spacing: 1px;
  }
  .vintage {
    margin-top: 46px;
    background: var(--ink); color: var(--cream);
    font-family: "Oswald", sans-serif; font-weight: 500;
    font-size: 22px; letter-spacing: 2px;
    padding: 4px 26px; border-radius: 3px;
    line-height: 1.2;
  }
  .abv { margin-top: 12px; font-size: 15px; }
  .flourish {
    width: 60px; height: 16px; border-radius: 8px;
    background: var(--ornament);
  }
  .front__content .flourish { margin-top: 28px; }
  /* back label */
  .label--back { background: var(--ink); color: var(--gold-text); }
  .back__frame {
    position: absolute; inset: 20px;
    border: 1.5px solid var(--gold);
  }
  .back__content {
    position: absolute; inset: 20px;
    display: flex; flex-direction: column; align-items: center;
    text-align: center; padding-top: 16px;
    font-weight: 700; font-size: 15px; line-height: 1.5;
    white-space: nowrap;
  }
  .warning__title { color: var(--wine-red); font-size: 15px; }
  .sulfites { margin-top: 16px; }
  .volume {
    margin-top: 16px;
    font-family: "Oswald", sans-serif; font-weight: 500;
    font-size: 28px; line-height: 1; letter-spacing: -.5px;
  }
  .back__content .flourish { margin-top: 10px; background: #6d6250; }
  .back__rule {
    position: absolute; left: 52px; right: 52px; bottom: 30px;
    height: 2px; background: var(--gold);
  }
</style>
</head>
<body>

  <section class="label label--front" aria-label="Sauvignon Blanc front label">
    <div class="label__frame"></div>
    <div class="corner-ornament corner-ornament--tl" role="img" aria-label="scroll corner ornament"></div>
    <div class="corner-ornament corner-ornament--tr" role="img" aria-label="scroll corner ornament"></div>
    <div class="corner-ornament corner-ornament--bl" role="img" aria-label="scroll corner ornament"></div>
    <div class="corner-ornament corner-ornament--br" role="img" aria-label="scroll corner ornament"></div>
    <div class="front__content">
      <div class="brand-mark">
        <span class="brand-mark__dot"></span>
        <span class="brand-mark__name">Brindor Ranch</span>
      </div>
      <h1 class="varietal">SAUVIGNON BLANC</h1>
      <p class="region">PALOS VERDES PENINSULA</p>
      <p class="vintage">YEAR 2022</p>
      <p class="abv">Alc. 12.5% by Vol.</p>
      <div class="flourish" role="img" aria-label="small swirl flourish"></div>
    </div>
  </section>

  <section class="label label--front" aria-label="Cabernet Sauvignon front label">
    <div class="label__frame"></div>
    <div class="corner-ornament corner-ornament--tl" role="img" aria-label="scroll corner ornament"></div>
    <div class="corner-ornament corner-ornament--tr" role="img" aria-label="scroll corner ornament"></div>
    <div class="corner-ornament corner-ornament--bl" role="img" aria-label="scroll corner ornament"></div>
    <div class="corner-ornament corner-ornament--br" role="img" aria-label="scroll corner ornament"></div>
    <div class="front__content">
      <div class="brand-mark">
        <span class="brand-mark__dot"></span>
        <span class="brand-mark__name">Brindor Ranch</span>
      </div>
      <h1 class="varietal">CABERNET SAUVIGNON</h1>
      <p class="region">PALOS VERDES PENINSULA</p>
      <p class="vintage">YEAR 2022</p>
      <p class="abv">Alc. 13.5% by Vol.</p>
      <div class="flourish" role="img" aria-label="small swirl flourish"></div>
    </div>
  </section>

  <section class="label label--back" aria-label="Back label">
    <div class="back__frame"></div>
    <div class="back__content">
      <p class="warning__title">GOVERNMENT WARNING</p>
      <p class="warning__text">(1) According to the Surgeon<br>General, women<br>should not drink alcoholic<br>beverages during pregnancy<br>because of the risk of<br>birth defects.<br>(2) Consumption of alcoholic<br>beverages impairs your ability<br>to<br>drive a car or operate machin-<br>ery, and may cause health<br>problems.</p>
      <p class="sulfites">Contains Sulfates.</p>
      <p class="volume">750ML</p>
      <div class="flourish" role="img" aria-label="small swirl flourish"></div>
    </div>
    <div class="back__rule"></div>
  </section>

</body>
</html>
```